Quorvex clinic business card - double sided for young clinic

I require business cards for my aesthetic clinic specialising in the below treatments. I would like the cards to be modern as my clinic base are young 22-35 years old. I require my logo on it and would like the edges to be rounded.

I have an aesthetic clinic specialising in :
Quorvex
Lip Enhancement
Chemical Peels
Facial Fillers
Non Surgical Face Lift

I would the cards to have the following information on them:
My logo - (in grey/silver)
address
Phone number
services

Colours :
White/grey/silver and red

a nice image on there, perhaps a set of lips as this is a main service i deliver

Company Name: PDA Address: 52 Farrowmere Road, 4 Brackwell High Street, KT9 4WQ Phone: 0208 794 2160 Website: www.penningtondoweaesthetics.co.uk

Target Market(s)

clinics 22-45 years old mainly female

Industry/Entity Type

Business

Contact Information for Business Card

as above

Requirements
Must have
• logo
• Address
• Email
• Phone number
• Services i offer
Nice to have
• images

```html
<!DOCTYPE html>
<html lang="en">
<head>
<meta charset="utf-8">
<title>PDA Business Card</title>
<link href="https://fonts.googleapis.com/css2?family=Open+Sans:wght@400;600;700&display=swap" rel="stylesheet">
<style>
  :root {
    --bg: #e9e9ea;
    --card: #ffffff;
    --silver: #a7a8ab;
    --silver-light: #c4c5c8;
    --charcoal: #3a3b3d;
    --ink: #333333;
    --red: #e8293b;
    --rule: #555555;
  }
  * { margin: 0; padding: 0; box-sizing: border-box; }
  html, body { width: 1200px; height: 913px; overflow: hidden; }
  body {
    background: var(--bg);
    font-family: "Open Sans", Arial, sans-serif;
    color: var(--ink);
    position: relative;
  }
  .card {
    position: absolute;
    width: 540px;
    height: 309px;
    background: var(--card);
    border-radius: 22px;
    overflow: hidden;
    box-shadow: 0 6px 18px rgba(0,0,0,.12);
  }
  .card--front { left: 40px; top: 302px; }
  .card--back { left: 620px; top: 302px; }
  .card__shapes { position: absolute; inset: 0; }

  .brand { position: absolute; display: flex; align-items: center; gap: 14px; }
  .brand__mark { width: 58px; height: 58px; border-radius: 50%; background: var(--silver-light); flex: none; }
  .brand__name {
    color: var(--silver);
    font-weight: 600;
    font-size: 14px;
    line-height: 1.3;
    letter-spacing: 1.5px;
    text-transform: uppercase;
  }
  .card--front .brand { left: 30px; top: 44px; }
  .card--back .brand { left: 34px; top: 118px; }
  .card--back .brand__mark { width: 72px; height: 72px; }
  .card--back .brand__name { font-size: 15px; letter-spacing: 1.2px; }

  .person { position: absolute; right: 34px; top: 38px; text-align: right; }
  .person__name { font-weight: 700; font-size: 20px; letter-spacing: .5px; color: var(--ink); }
  .person__role { font-size: 11px; color: var(--red); letter-spacing: 1px; text-transform: uppercase; }
  .divider { position: absolute; left: 30px; right: 34px; top: 118px; border-top: 1px solid var(--rule); }

  .contact { position: absolute; left: 30px; top: 134px; font-size: 14px; line-height: 1.45; }
  .contact__address { margin-bottom: 10px; }
  .contact__row { display: flex; align-items: center; gap: 8px; font-size: 14px; }
  .contact__row svg { width: 12px; height: 12px; flex: none; }

  .services { position: absolute; left: 340px; top: 58px; font-size: 14px; line-height: 1.45; }
  .services__title { margin-bottom: 2px; }
  .services__list { list-style: none; }
  .services__list li { display: flex; align-items: center; gap: 8px; }
  .services__list li::before {
    content: ""; width: 9px; height: 9px; border-radius: 50%; background: var(--red); flex: none;
  }
</style>
</head>
<body>

<section class="card card--front" aria-label="Business card front">
  <svg class="card__shapes" viewBox="0 0 540 309" aria-hidden="true">
    <rect x="200" y="268" width="290" height="41" fill="var(--charcoal)"/>
    <path d="M0 262 H180 Q220 262 232 290 L240 309 H0 Z" fill="var(--silver)"/>
    <path d="M540 190 H500 Q470 190 468 222 V309 H540 Z" fill="var(--silver)"/>
  </svg>
  <div class="person">
    <div class="person__name">MIRA HALE</div>
    <div class="person__role">Owner</div>
  </div>
  <div class="brand">
    <span class="brand__mark"></span>
    <span class="brand__name">PDA<br>Pennington Dowe<br>Aesthetics</span>
  </div>
  <div class="divider"></div>
  <div class="contact">
    <div class="contact__address">52 Farrowmere Road<br>4 Brackwell High Street, KT9 4WQ</div>
    <div class="contact__row">
      <svg viewBox="0 0 12 12"><path d="M2.5 1 L4.5 1 L5.2 3.6 L3.9 4.6 Q5 7 7.4 8.1 L8.4 6.8 L11 7.5 V9.5 Q11 11 9.5 11 Q1 10 1 2.5 Q1 1 2.5 1Z" fill="var(--red)"/></svg>
      <span>0208 794 2160</span>
    </div>
    <div class="contact__row">
      <svg viewBox="0 0 12 12"><circle cx="6" cy="6" r="5.2" fill="var(--red)"/><path d="M1 6 H11 M6 1 Q3 6 6 11 M6 1 Q9 6 6 11" stroke="#fff" stroke-width=".8" fill="none"/></svg>
      <span>www.penningtondoweaesthetics.co.uk</span>
    </div>
  </div>
</section>

<section class="card card--back" aria-label="Business card back">
  <svg class="card__shapes" viewBox="0 0 540 309" aria-hidden="true">
    <rect x="200" y="268" width="290" height="41" fill="var(--charcoal)"/>
    <path d="M0 262 H180 Q220 262 232 290 L240 309 H0 Z" fill="var(--silver)"/>
    <path d="M540 190 H500 Q470 190 468 222 V309 H540 Z" fill="var(--silver)"/>
  </svg>
  <div class="brand">
    <span class="brand__mark"></span>
    <span class="brand__name">PDA<br>Pennington Dowe<br>Aesthetics</span>
  </div>
  <div class="services">
    <div class="services__title">Specializing in:</div>
    <ul class="services__list">
      <li>Quorvex</li>
      <li>Lip Enhancement</li>
      <li>Chemical Peels</li>
      <li>Facial Fillers</li>
      <li>Non-Surgical Face Lift</li>
    </ul>
  </div>
</section>

</body>
</html>
```